Oil Field Service company needs professional business cards

Looking to clean up our current company business cards and look a little more professional. Harlow Casing Services is a US based company that services the oil field. We deal with engineers, managers and oil rigs....................................................................................................................................................................................................................................................................................................................................................................................................

Target Market(s)

Oil and Gas professionals

Industry/Entity Type

Oil And Gas

Contact Information for Business Card

See attached photo as example

Font styles to use
Sans Serif

Colors
ec1f27

Requirements
Must have
• Company Logo, Name, Title, Cell, Office, Fax, Email.
• See attached photo
Nice to have
• External CRT, Internal CRT, Casing Crews, Torque Turn, Laydown Machine
Should not have
• Do not introduce any new pictures and keep it professional looking

```html
<!DOCTYPE html>
<html lang="en">
<head>
<meta charset="utf-8">
<title>Harlow Casing Services – Business Card</title>
<link href="https://fonts.googleapis.com/css2?family=Roboto:wght@400;700;900&display=swap" rel="stylesheet">
<style>
  :root{
    --brand-red:#ec1f27;
    --slate:#3b4550;
    --ink:#222;
    --paper:#ffffff;
    --backdrop:#e9e9eb;
  }
  *{box-sizing:border-box;margin:0;padding:0}
  html,body{width:1200px;height:900px;overflow:hidden}
  body{background:var(--backdrop);font-family:"Roboto",Arial,sans-serif;display:flex;align-items:center;justify-content:center}
  .card{position:relative;width:1050px;height:600px;background:var(--paper);box-shadow:0 10px 30px rgba(0,0,0,.18);overflow:hidden}
  .contact-band{position:absolute;top:0;left:0;right:0;height:44px;background:var(--brand-red)}
  .contact-item{position:absolute;top:0;height:44px;display:flex;flex-direction:column;align-items:center}
  .contact-text{color:#fff;font-weight:700;font-size:17px;line-height:44px;white-space:nowrap}
  .contact-icon{position:absolute;top:30px;width:34px;height:34px;border-radius:50%;background:var(--brand-red);border:3px solid #fff;display:flex;align-items:center;justify-content:center}
  .contact-icon svg{width:17px;height:17px;fill:#fff}
  .c1{left:60px}.c2{left:330px}.c3{left:600px}.c4{right:40px}
  .identity{position:absolute;top:150px;left:0;right:0;text-align:center}
  .company-name{display:inline-flex;align-items:center;gap:16px;color:var(--slate);font-weight:900;font-size:52px;letter-spacing:1px;text-transform:uppercase}
  .company-dot{width:22px;height:22px;border-radius:50%;background:var(--brand-red)}
  .person{margin-top:70px}
  .person-name{color:var(--brand-red);font-weight:700;font-size:34px}
  .person-title{color:var(--ink);font-size:20px;margin-top:6px}
  .services-band{position:absolute;bottom:0;left:0;right:0;height:56px;background:var(--brand-red);display:flex;align-items:center;justify-content:space-evenly;padding:0 20px}
  .service{color:#fff;font-weight:700;font-size:19px;white-space:nowrap}
  .service-dot{width:11px;height:11px;border-radius:50%;background:#fff}
</style>
</head>
<body>
  <main class="card">
    <header class="contact-band">
      <div class="contact-item c1"><span class="contact-text">555-210-4780</span>
        <span class="contact-icon"><svg viewBox="0 0 24 24"><path d="M6.6 10.8c1.4 2.8 3.8 5.1 6.6 6.6l2.2-2.2c.3-.3.7-.4 1-.2 1.1.4 2.3.6 3.6.6.6 0 1 .4 1 1V20c0 .6-.4 1-1 1C10.6 21 3 13.4 3 4c0-.6.4-1 1-1h3.5c.6 0 1 .4 1 1 0 1.3.2 2.5.6 3.6.1.3 0 .7-.2 1z"/></svg></span></div>
      <div class="contact-item c2"><span class="contact-text">555-210-4781</span>
        <span class="contact-icon"><svg viewBox="0 0 24 24"><path d="M3 8c0-2 4-4 9-4s9 2 9 4v2h-5V8H8v2H3z"/><rect x="5" y="12" width="14" height="8" rx="1"/></svg></span></div>
      <div class="contact-item c3"><span class="contact-text">555-210-4782</span>
        <span class="contact-icon"><svg viewBox="0 0 24 24"><rect x="7" y="2" width="10" height="7"/><rect x="3" y="10" width="18" height="8" rx="1"/><rect x="7" y="15" width="10" height="7"/></svg></span></div>
      <div class="contact-item c4"><span class="contact-text">gellis@harlowcasing.com</span>
        <span class="contact-icon"><svg viewBox="0 0 24 24"><path d="M2 5h20v14H2z M4 7v1l8 5 8-5V7l-8 5z" fill-rule="evenodd"/></svg></span></div>
    </header>

    <section class="identity">
      <div class="company-name"><span class="company-dot"></span>Harlow Casing Services</div>
      <div class="person">
        <div class="person-name">Grant R. Ellis</div>
        <div class="person-title">CFO / Founder</div>
      </div>
    </section>

    <footer class="services-band">
      <span class="service">External CRT</span><span class="service-dot"></span>
      <span class="service">Internal CRT</span><span class="service-dot"></span>
      <span class="service">Casing Crews</span><span class="service-dot"></span>
      <span class="service">Torque Turn</span><span class="service-dot"></span>
      <span class="service">Laydown Machine</span>
    </footer>
  </main>
</body>
</html>
```